Lumora Activewear business card design

I need a business card designed for my activewear business. I would like to use the colours pink, purple white and blue. please see attached logo. please include (name) Harriet Welloby (phone) 0417582064 (email) hattieslumora@mailvento.com (ABN) 48715290637 . please include - Free shipping on all orders over $100

Target Market(s)

female

Contact Information for Business Card

Colors

Requirements
Must have
• I need a business card designed for my activewear business. I would like to use the colours pink, purple white and blue. please see attached logo. please include (name) Harriet Welloby (phone) 0417582064 (email) hattieslumora@mailvento.com (ABN) 48715290637 . please include - Free shipping on all orders over $100

```html
<!DOCTYPE html>
<html lang="en">
<head>
<meta charset="utf-8">
<title>Lumora Activewear – Business Card</title>
<link rel="stylesheet" href="https://fonts.googleapis.com/css2?family=Lato:wght@400;700;900&display=swap">
<style>
  :root {
    --stage: #e6e4e8;
    --card-white: #ffffff;
    --purple: #9a1bb0;
    --purple-deep: #7d1a99;
    --magenta: #b2347f;
    --pink: #c0407e;
    --ink: #2b2b2b;
    --rule: #dcdcdc;
    --shadow: 0 6px 18px rgba(0,0,0,.18);
  }
  * { box-sizing: border-box; margin: 0; padding: 0; }
  html, body { width: 1200px; height: 782px; overflow: hidden; }
  body {
    background: var(--stage);
    font-family: "Lato", sans-serif;
    position: relative;
  }
  .card {
    position: absolute;
    top: 240px;
    width: 530px;
    height: 303px;
    box-shadow: var(--shadow);
    overflow: hidden;
  }
  /* Front */
  .card--front { left: 45px; background: var(--card-white); }
  .brand {
    position: absolute;
    left: 0; top: 0;
    width: 248px; height: 228px;
    display: flex; align-items: center; justify-content: center;
    gap: 10px;
  }
  .brand__dot {
    width: 14px; height: 14px; border-radius: 50%;
    background: var(--purple);
  }
  .brand__name {
    font-weight: 900;
    font-size: 40px;
    letter-spacing: 2px;
    color: var(--purple);
  }
  .divider {
    position: absolute;
    left: 252px; top: 60px;
    width: 1px; height: 108px;
    background: var(--rule);
  }
  .contact {
    position: absolute;
    left: 272px; top: 78px;
    color: var(--ink);
    font-size: 15px;
    line-height: 21px;
  }
  .contact__name {
    font-weight: 900;
    font-size: 17px;
    letter-spacing: 1px;
    color: var(--purple);
    text-transform: uppercase;
    margin-bottom: 6px;
  }
  .contact__line { display: flex; align-items: center; gap: 6px; }
  .contact__icon { width: 11px; height: 11px; fill: var(--purple); flex: none; }
  .contact__label { color: var(--pink); }
  .offer-band {
    position: absolute;
    left: 0; bottom: 0;
    width: 100%; height: 70px;
    background: var(--magenta);
    border-top: 3px solid var(--purple);
    display: flex; align-items: center;
    padding-left: 70px;
    color: #fff;
    font-size: 15px;
    letter-spacing: .5px;
    text-transform: uppercase;
  }
  /* Back */
  .card--back { left: 625px; }
  .back-pattern {
    position: absolute; inset: 0;
    background: linear-gradient(200deg, var(--purple) 0%, #a5249f 45%, var(--pink) 100%);
  }
</style>
</head>
<body>
  <section class="card card--front" aria-label="Business card front">
    <div class="brand">
      <span class="brand__dot"></span>
      <span class="brand__name">LUMORA</span>
    </div>
    <div class="divider"></div>
    <div class="contact">
      <p class="contact__name">Harriet Welloby</p>
      <p class="contact__line">
        <svg class="contact__icon" viewBox="0 0 24 24" aria-hidden="true"><path d="M6.6 10.8a15.1 15.1 0 0 0 6.6 6.6l2.2-2.2a1 1 0 0 1 1-.25 11.4 11.4 0 0 0 3.6.57 1 1 0 0 1 1 1V20a1 1 0 0 1-1 1A17 17 0 0 1 3 4a1 1 0 0 1 1-1h3.5a1 1 0 0 1 1 1c0 1.25.2 2.45.57 3.57a1 1 0 0 1-.25 1z"/></svg>
        0417582064
      </p>
      <p class="contact__line">
        <svg class="contact__icon" viewBox="0 0 24 24" aria-hidden="true"><path d="M2 5h20v14H2z M2 5l10 8 10-8" fill="var(--purple)"/><path d="M3 6l9 7 9-7" stroke="#fff" stroke-width="2" fill="none"/></svg>
        hattieslumora@mailvento.com
      </p>
      <p class="contact__line"><span class="contact__label">ABN:</span> 48715290637</p>
    </div>
    <div class="offer-band">Free shipping on all orders over $100</div>
  </section>

  <section class="card card--back" aria-label="Business card back">
    <div class="back-pattern" role="img" aria-label="Purple to pink gradient with a faint repeating brand pattern"></div>
  </section>
</body>
</html>
```